Cleaning Company needs a new business card design

Hi, We are looking for new business card designs to update with our latest logo and company information.
We would like to see designs using the colours:
Royal Blue #4169E1 - this is our company colour so this has to be in there. Please feel free to experiment with other colours.
Must include:
Front of business card:
Logo
Back of the business card:
0800 519 2867
07946 581 302
Email: info@pelvormaids.co.uk
Web: www.pelvormaids.co.uk
Services:
End of Tenancy
Carpet & Upholstery
Regular & One Off
all work fully insured.
The front of the business card with the logo can be made to look raised print. The blue man to be a shiny finish.
The business card needs to be presented in a matt finish
The business must be in the following styles:
Standard Square with rounded corners.
Thank you to all that take part in this.
Target Market(s)
Men and Women of different ages in the UK.
Industry/Entity Type
House Cleaning
Contact Information for Business Card
Front of business card:
Logo
0800 519 2867
07946 581 302
Email: pelvormaids@brimmail.co.uk
Services:
End of Tenancy
Carpet & Upholstery
Regular & One Off
all work fully insured.

```html
<!DOCTYPE html>
<html lang="en">
<head>
<meta charset="utf-8">
<title>Pelvor Maids Limited – Business Card</title>
<link rel="stylesheet" href="https://fonts.googleapis.com/css2?family=Lato:wght@400;700&display=swap">
<style>
  :root {
    --backdrop: #5b4a3c;
    --card-white: #ffffff;
    --brand-blue: #0656a4;
    --heading-blue: #1b4f9c;
    --icon-blue: #2aa3e0;
    --ink: #2b2b2b;
    --rule: #e4e7ec;
  }
  html, body {
    margin: 0;
    width: 1200px;
    height: 1000px;
    overflow: hidden;
    background: var(--backdrop);
    font-family: "Lato", sans-serif;
  }
  .canvas {
    position: relative;
    width: 1200px;
    height: 1000px;
  }
  .card {
    position: absolute;
    left: 242px;
    width: 716px;
    height: 408px;
    border-radius: 30px;
    box-sizing: border-box;
  }
  .card--details {
    top: 82px;
    background: var(--card-white);
  }
  .card--logo {
    top: 511px;
    background: var(--brand-blue);
    display: flex;
    align-items: center;
    justify-content: center;
  }
  .details {
    position: absolute;
    left: 356px;
    top: 74px;
    width: 300px;
  }
  .contact-list, .service-list {
    list-style: none;
    margin: 0;
    padding: 0;
  }
  .contact-list li, .service-list li {
    display: flex;
    align-items: center;
    height: 25.7px;
    font-size: 17px;
    color: var(--ink);
  }
  .contact-list svg {
    width: 13px;
    height: 13px;
    margin-right: 6px;
    flex: none;
    fill: var(--icon-blue);
  }
  .divider {
    width: 252px;
    height: 1px;
    margin: 24px 0 22px;
    background: linear-gradient(to right, var(--rule), var(--rule) 80%, rgba(228,231,236,0));
    border: 0;
  }
  .services-title {
    margin: 0 0 6px;
    font-size: 16px;
    font-weight: 400;
    letter-spacing: 0.5px;
    color: var(--heading-blue);
  }
  .service-list svg {
    width: 13px;
    height: 13px;
    margin-right: 8px;
    flex: none;
  }
  .brand {
    display: flex;
    align-items: center;
    gap: 16px;
    margin-top: 40px;
  }
  .brand-dot {
    width: 22px;
    height: 22px;
    border-radius: 50%;
    background: var(--icon-blue);
  }
  .brand-name {
    font-size: 46px;
    font-weight: 700;
    color: var(--card-white);
    letter-spacing: 0.5px;
  }
</style>
</head>
<body>
<div class="canvas">

  <section class="card card--details" aria-label="Back of business card">
    <div class="details">
      <ul class="contact-list">
        <li>
          <svg viewBox="0 0 16 16" aria-hidden="true"><path d="M4 0h8a1.5 1.5 0 0 1 1.5 1.5v13A1.5 1.5 0 0 1 12 16H4a1.5 1.5 0 0 1-1.5-1.5v-13A1.5 1.5 0 0 1 4 0zm0 2v10.5h8V2zm4 11.3a.9.9 0 1 0 0 1.8.9.9 0 0 0 0-1.8z"/></svg>
          0800 519 2867
        </li>
        <li>
          <svg viewBox="0 0 16 16" aria-hidden="true"><path d="M3.6 1.2l2.3 2.6-1.3 1.8c.9 2 2.6 3.7 4.6 4.6l1.8-1.3 2.6 2.3-1.5 2.4C7 13.5 2.5 9 1.2 3.1z"/></svg>
          07946 581 302
        </li>
        <li>
          <svg viewBox="0 0 16 16" aria-hidden="true"><path d="M1 3h14v10H1zm1.5 1.4v.2L8 8.6l5.5-4V4.4zm0 2v5.1h11V6.4L8 10.3z"/></svg>
          pelvormaids@brimmail.co.uk
        </li>
        <li>
          <svg viewBox="0 0 16 16" aria-hidden="true"><path d="M8 1a7 7 0 1 0 0 14A7 7 0 0 0 8 1zm0 1.3c.8.8 1.4 2.1 1.6 3.7H6.4C6.6 4.4 7.2 3.1 8 2.3zM5 6H2.6A5.7 5.7 0 0 1 6 2.6C5.5 3.5 5.1 4.7 5 6zm0 1.3c0 .5 0 1 .1 1.4H2.4a5.7 5.7 0 0 1 0-1.4zm1.3 0h3.4a8 8 0 0 1 0 1.4H6.3a8 8 0 0 1 0-1.4zm4.7 0h2.6a5.7 5.7 0 0 1 0 1.4H11zm0-1.3c-.1-1.3-.5-2.5-1-3.4A5.7 5.7 0 0 1 13.4 6zM2.6 10H5c.1 1.3.5 2.5 1 3.4A5.7 5.7 0 0 1 2.6 10zm3.8 0h3.2c-.2 1.6-.8 2.9-1.6 3.7-.8-.8-1.4-2.1-1.6-3.7zm4.6 0h2.4A5.7 5.7 0 0 1 10 13.4c.5-.9.9-2.1 1-3.4z"/></svg>
          www.pelvormaids.co.uk
        </li>
      </ul>

      <hr class="divider">

      <h2 class="services-title">SERVICES</h2>
      <ul class="service-list">
        <li><svg viewBox="0 0 16 16" aria-hidden="true"><path d="M2 8.5l4 4L14.5 3" fill="none" stroke="var(--icon-blue)" stroke-width="2.6" stroke-linecap="round" stroke-linejoin="round"/></svg>End of Tenancy</li>
        <li><svg viewBox="0 0 16 16" aria-hidden="true"><path d="M2 8.5l4 4L14.5 3" fill="none" stroke="var(--icon-blue)" stroke-width="2.6" stroke-linecap="round" stroke-linejoin="round"/></svg>Carpet &amp; Upholstery</li>
        <li><svg viewBox="0 0 16 16" aria-hidden="true"><path d="M2 8.5l4 4L14.5 3" fill="none" stroke="var(--icon-blue)" stroke-width="2.6" stroke-linecap="round" stroke-linejoin="round"/></svg>Regular &amp; One Off</li>
      </ul>
    </div>
  </section>

  <section class="card card--logo" aria-label="Front of business card">
    <div class="brand">
      <span class="brand-dot" aria-hidden="true"></span>
      <span class="brand-name">Pelvor Maids Limited</span>
    </div>
  </section>

</div>
</body>
</html>
```